Aged Care Consultancy Business needs a business card design

I need a two sided business card - I want it clean and professional. Surprise me

Target Market(s)

middle aged and ageing victorians

Industry/Entity Type

Health Care

Contact Information for Business Card

Text to be included

Logo
Aged Care Consulting Services
Professional, Reliable, Affordable

Tovan Brelsick
Director
0427 31 64 92 (larger)
1300 73 29 41
tovan@wadolire.com.au
www.wadolcare.com.au
Facebook (details TBA)

include little icons beside the contact info:

- Envelope = email
- Phone = phone
- Globe = website

Font styles to use
Serif
Sans Serif

Requirements
Must have
• look proffesional and clean

```html
<!DOCTYPE html>
<html lang="en">
<head>
<meta charset="utf-8">
<title>Wadol Care – Business Card</title>
<link href="https://fonts.googleapis.com/css2?family=Questrial&display=swap" rel="stylesheet">
<style>
  :root {
    --backdrop: #b1b1b1;
    --brand-blue: #1c3f78;
    --brand-blue-deep: #173566;
    --brand-orange: #e6901e;
    --ink-navy: #213a73;
    --card-white: #f3f3f3;
    --text-light: #e9eef7;
  }
  html, body {
    margin: 0;
    padding: 0;
    width: 1200px;
    height: 1050px;
    overflow: hidden;
    background: var(--backdrop);
    font-family: "Questrial", "Century Gothic", sans-serif;
  }
  .canvas {
    position: relative;
    width: 1200px;
    height: 1050px;
  }
  .card {
    position: absolute;
    left: 264px;
    width: 672px;
    height: 384px;
    border-radius: 38px;
    overflow: hidden;
  }
  .card--front { top: 110px; background: var(--card-white); }
  .card--back {
    top: 574px;
    background: radial-gradient(ellipse at center, #1f4580 0%, var(--brand-blue) 60%, var(--brand-blue-deep) 100%);
  }
  .card__waves {
    position: absolute;
    inset: 0;
  }
  .brand-name {
    position: absolute;
    margin: 0;
    white-space: nowrap;
    letter-spacing: 0.5px;
  }
  .card--front .brand-name {
    left: 46px;
    top: 104px;
    font-size: 40px;
    color: var(--ink-navy);
  }
  .brand-mark {
    position: absolute;
    border-radius: 50%;
  }
  .card--front .brand-mark {
    left: 48px;
    top: 46px;
    width: 50px;
    height: 50px;
    background: var(--brand-orange);
  }
  .tagline {
    position: absolute;
    left: 46px;
    top: 164px;
    margin: 0;
    font-size: 13px;
    color: var(--ink-navy);
  }
  .tagline__accent { color: var(--brand-orange); }
  .person {
    position: absolute;
    left: 46px;
    top: 252px;
    color: var(--text-light);
  }
  .person__name { margin: 0; font-size: 22px; line-height: 24px; }
  .person__role { margin: 0; font-size: 16px; line-height: 20px; }
  .address {
    position: absolute;
    left: 46px;
    top: 320px;
    margin: 0;
    font-size: 16px;
    line-height: 20px;
    font-style: normal;
    color: var(--text-light);
  }
  .contacts {
    position: absolute;
    left: 242px;
    top: 282px;
    margin: 0;
    padding: 0;
    list-style: none;
    color: var(--text-light);
    font-size: 16px;
  }
  .contacts__item {
    display: flex;
    align-items: center;
    height: 20px;
  }
  .contacts__icon {
    width: 16px;
    height: 16px;
    margin-right: 10px;
    fill: var(--text-light);
    stroke: var(--text-light);
  }
  .card--back .brand-mark {
    left: 311px;
    top: 132px;
    width: 50px;
    height: 50px;
    background: var(--brand-orange);
  }
  .card--back .brand-name {
    left: 0;
    right: 0;
    top: 198px;
    text-align: center;
    font-size: 54px;
    color: #ffffff;
  }
  .social-link {
    position: absolute;
    left: 0;
    right: 0;
    top: 342px;
    margin: 0;
    text-align: center;
    font-size: 16px;
    color: var(--text-light);
  }
</style>
</head>
<body>
<main class="canvas">

  <section class="card card--front" aria-label="Business card front">
    <svg class="card__waves" viewBox="0 0 672 384" width="672" height="384" aria-hidden="true">
      <defs>
        <linearGradient id="paper" x1="0" y1="0" x2="1" y2="1">
          <stop offset="0" stop-color="#ececec"/>
          <stop offset="0.5" stop-color="#f7f7f7"/>
          <stop offset="1" stop-color="#e6e6e6"/>
        </linearGradient>
      </defs>
      <rect width="672" height="384" fill="url(#paper)"/>
      <path d="M0,226 Q300,252 672,94 L672,384 L0,384 Z" fill="var(--brand-blue)"/>
      <path d="M0,183 Q330,232 672,90 Q320,252 0,218 Z" fill="var(--brand-orange)"/>
    </svg>

    <span class="brand-mark" aria-hidden="true"></span>
    <h1 class="brand-name">wadol care</h1>
    <p class="tagline">Professional, <span class="tagline__accent">Reliable</span>, Affordable</p>

    <div class="person">
      <p class="person__name">Tovan Brelsick</p>
      <p class="person__role">Director</p>
    </div>
    <address class="address">Here your company<br>or home address</address>

    <ul class="contacts">
      <li class="contacts__item">
        <svg class="contacts__icon" viewBox="0 0 16 16" aria-hidden="true"><rect x="1" y="1" width="4" height="14" rx="1" stroke="none"/><rect x="6" y="3" width="9" height="12" rx="1" fill="none" stroke-width="1.5"/><rect x="8" y="5" width="5" height="2" stroke="none"/><rect x="8" y="9" width="5" height="4" stroke="none"/></svg>
        <span>0427 31 64 92</span>
      </li>
      <li class="contacts__item">
        <svg class="contacts__icon" viewBox="0 0 16 16" aria-hidden="true"><path stroke="none" d="M3.5 1 L6 4.5 L4.6 6.2 Q6.2 9.6 9.8 11.4 L11.5 10 L15 12.5 L13.4 15 Q6.5 14.5 1.5 6 Q1 3 3.5 1 Z"/></svg>
        <span>1300 73 29 41</span>
      </li>
      <li class="contacts__item">
        <svg class="contacts__icon" viewBox="0 0 16 16" aria-hidden="true"><rect x="1" y="3.5" width="14" height="9" stroke="none"/><path d="M1 3.5 L8 9 L15 3.5" fill="none" stroke="var(--brand-blue)" stroke-width="1.2"/></svg>
        <span>tovan@wadolire.com.au</span>
      </li>
      <li class="contacts__item">
        <svg class="contacts__icon" viewBox="0 0 16 16" aria-hidden="true" fill="none"><circle cx="8" cy="8" r="6.5" stroke-width="1.2"/><ellipse cx="8" cy="8" rx="3" ry="6.5" stroke-width="1"/><path d="M1.5 8 H14.5 M2.5 4.8 H13.5 M2.5 11.2 H13.5" stroke-width="1"/></svg>
        <span>www.wadolcare.com.au</span>
      </li>
    </ul>
  </section>

  <section class="card card--back" aria-label="Business card back">
    <span class="brand-mark" aria-hidden="true"></span>
    <h2 class="brand-name">wadol care</h2>
    <p class="social-link">www.friendlink.com/wadolcare</p>
  </section>

</main>
</body>
</html>
```